Steady Pathways, Inc
Steady Pathways
Bright & Fun-filled
Marisa Delacorte
P.O. Box 38216
4873-B Thimble Crest Road
Goldsboro, NC 27845
madelacorte@steadypathwaysgrp.net
"Press Toward The Mark A+"
Logo File.

```html
<!DOCTYPE html>
<html lang="en">
<head>
<meta charset="utf-8">
<title>Steady Pathways, Inc — Stationery Set</title>
<link href="https://fonts.googleapis.com/css2?family=Open+Sans:wght@400;700&display=swap" rel="stylesheet">
<style>
  :root{
    --navy:#25307a;
    --red:#e2323a;
    --paper:#ffffff;
    --ink:#4a4f63;
    --bg:#efeae2;
    --shadow:rgba(60,40,20,.22);
    --mark:#dfe3f1;
  }
  *{margin:0;padding:0;box-sizing:border-box}
  html,body{width:1200px;height:346px;overflow:hidden;background:var(--bg);font-family:"Open Sans",Arial,sans-serif;color:var(--ink)}
  .sheet{position:absolute;background:var(--paper);box-shadow:1px 2px 4px var(--shadow);overflow:hidden}
  .sheet svg.trim{position:absolute;inset:0;width:100%;height:100%}
  .brand{position:absolute;display:flex;align-items:center;gap:3px;color:var(--navy);font-weight:700;white-space:nowrap;line-height:1}
  .brand .dot{border-radius:50%;background:var(--red);flex:none}
  .tagline{position:absolute;font-size:4px;color:var(--ink);white-space:nowrap}
  .watermark{position:absolute;border-radius:50%;background:var(--mark);opacity:.7}
  .footer-info{position:absolute;left:0;right:0;text-align:center;font-size:3.6px;line-height:1.35;color:var(--ink)}

  /* letterheads */
  .letterhead{top:7px;width:216px;height:293px}
  .letterhead.first{left:137px}
  .letterhead.second{left:365px}
  .letterhead .brand{left:16px;top:14px;font-size:11px}
  .letterhead .brand .dot{width:8px;height:8px}
  .letterhead .tagline{left:16px;top:28px}
  .letterhead .watermark{left:84px;top:122px;width:48px;height:48px}
  .letterhead .footer-info{bottom:12px}

  /* business cards */
  .card{left:7px;width:101px;height:56px}
  .card.front{top:100px}
  .card.back{top:175px}
  .card.front .brand{left:7px;top:8px;font-size:7px}
  .card.front .brand .dot{width:5px;height:5px}
  .card .person{position:absolute;left:7px;top:26px;font-size:4.4px;font-weight:700;color:var(--navy)}
  .card .details{position:absolute;left:7px;top:32px;font-size:3.2px;line-height:1.35}
  .card.back .name-line{position:absolute;left:0;right:0;top:20px;text-align:center;font-size:4.6px;font-weight:700;color:var(--navy)}
  .card.back .motto{position:absolute;left:0;right:0;top:28px;text-align:center;font-size:4px;color:var(--red);font-weight:700}

  /* envelope fronts */
  .envelope{left:612px;width:175px;height:94px}
  .envelope.upper{top:100px}
  .envelope.lower{top:232px}
  .envelope .brand{left:9px;top:9px;font-size:8px}
  .envelope .brand .dot{width:6px;height:6px}
  .envelope .return{position:absolute;left:9px;top:20px;font-size:3.4px;line-height:1.35}
  .envelope .watermark{left:72px;top:32px;width:32px;height:32px}

  /* envelope backs */
  .envelope-back{left:924px;width:168px}
  .envelope-back.navy{top:7px;height:100px}
  .envelope-back.red{top:124px;height:112px}
  .envelope-back.plain{top:244px;height:66px}
</style>
</head>
<body>

  <!-- business card front -->
  <section class="sheet card front">
    <svg class="trim" viewBox="0 0 101 56" preserveAspectRatio="none">
      <path d="M101 0 L101 56 L90 56 Q98 30 86 0 Z" fill="var(--navy)"/>
      <path d="M86 0 Q98 30 90 56 L87 56 Q94 30 82 0 Z" fill="var(--red)"/>
    </svg>
    <div class="brand"><span class="dot"></span>Steady Pathways</div>
    <div class="person">Marisa Delacorte</div>
    <div class="details">P.O. Box 38216<br>Goldsboro, NC 27845<br>madelacorte@steadypathwaysgrp.net</div>
  </section>

  <!-- business card back -->
  <section class="sheet card back">
    <svg class="trim" viewBox="0 0 101 56" preserveAspectRatio="none">
      <rect x="0" y="52" width="101" height="4" fill="var(--navy)"/>
      <rect x="0" y="50" width="101" height="2" fill="var(--red)"/>
    </svg>
    <div class="name-line">Steady Pathways, Inc</div>
    <div class="motto">"Press Toward The Mark A+"</div>
  </section>

  <!-- letterhead, first page -->
  <section class="sheet letterhead first">
    <svg class="trim" viewBox="0 0 216 293" preserveAspectRatio="none">
      <path d="M216 0 L216 150 Q206 60 176 0 Z" fill="var(--navy)"/>
      <path d="M170 0 L176 0 Q206 60 216 150 L216 160 Q202 65 170 0 Z" fill="var(--red)"/>
      <path d="M0 293 L0 150 Q10 233 40 293 Z" fill="var(--navy)"/>
      <path d="M46 293 L40 293 Q10 233 0 150 L0 140 Q14 228 46 293 Z" fill="var(--red)"/>
    </svg>
    <div class="brand"><span class="dot"></span>Steady Pathways</div>
    <div class="tagline">Bright &amp; Fun-filled</div>
    <div class="watermark"></div>
    <div class="footer-info">P.O. Box 38216 · 4873-B Thimble Crest Road<br>Goldsboro, NC 27845<br>madelacorte@steadypathwaysgrp.net</div>
  </section>

  <!-- letterhead, second page -->
  <section class="sheet letterhead second">
    <svg class="trim" viewBox="0 0 216 293" preserveAspectRatio="none">
      <path d="M216 0 L216 150 Q206 60 176 0 Z" fill="var(--navy)"/>
      <path d="M170 0 L176 0 Q206 60 216 150 L216 160 Q202 65 170 0 Z" fill="var(--red)"/>
      <path d="M0 293 L0 150 Q10 233 40 293 Z" fill="var(--navy)"/>
      <path d="M46 293 L40 293 Q10 233 0 150 L0 140 Q14 228 46 293 Z" fill="var(--red)"/>
    </svg>
    <div class="brand"><span class="dot"></span>Steady Pathways</div>
    <div class="tagline">Bright &amp; Fun-filled</div>
    <div class="watermark"></div>
    <div class="footer-info">P.O. Box 38216 · 4873-B Thimble Crest Road<br>Goldsboro, NC 27845<br>madelacorte@steadypathwaysgrp.net</div>
  </section>

  <!-- envelope fronts -->
  <section class="sheet envelope upper">
    <svg class="trim" viewBox="0 0 175 94" preserveAspectRatio="none">
      <path d="M175 0 L175 60 Q168 22 150 0 Z" fill="var(--navy)"/>
      <path d="M146 0 L150 0 Q168 22 175 60 L175 66 Q166 25 146 0 Z" fill="var(--red)"/>
    </svg>
    <div class="brand"><span class="dot"></span>Steady Pathways</div>
    <div class="return">P.O. Box 38216<br>4873-B Thimble Crest Road<br>Goldsboro, NC 27845</div>
    <div class="watermark"></div>
  </section>

  <section class="sheet envelope lower">
    <svg class="trim" viewBox="0 0 175 94" preserveAspectRatio="none">
      <path d="M175 0 L175 60 Q168 22 150 0 Z" fill="var(--navy)"/>
      <path d="M146 0 L150 0 Q168 22 175 60 L175 66 Q166 25 146 0 Z" fill="var(--red)"/>
    </svg>
    <div class="brand"><span class="dot"></span>Steady Pathways</div>
    <div class="return">P.O. Box 38216<br>4873-B Thimble Crest Road<br>Goldsboro, NC 27845</div>
    <div class="watermark"></div>
  </section>

  <!-- envelope backs -->
  <section class="sheet envelope-back navy">
    <svg class="trim" viewBox="0 0 168 100" preserveAspectRatio="none">
      <path d="M0 0 L168 0 L168 8 L84 62 L0 8 Z" fill="var(--navy)"/>
      <path d="M0 60 L70 100 M168 60 L98 100" stroke="#d8d8d8" stroke-width=".6" fill="none"/>
    </svg>
  </section>

  <section class="sheet envelope-back red">
    <svg class="trim" viewBox="0 0 168 112" preserveAspectRatio="none">
      <rect x="0" y="0" width="168" height="30" fill="var(--red)"/>
      <path d="M0 70 L70 112 M168 70 L98 112" stroke="#d8d8d8" stroke-width=".6" fill="none"/>
    </svg>
  </section>

  <section class="sheet envelope-back plain">
    <svg class="trim" viewBox="0 0 168 66" preserveAspectRatio="none">
      <path d="M0 0 L84 34 L168 0" stroke="#d0d0d0" stroke-width=".7" fill="none"/>
    </svg>
  </section>

</body>
</html>
```